TotBramble Needs a Banner Ad Design

We need a banner ad design for a new competition and will be placed on Facebook and at our website (totbramble.example).

Competition name: Support your community

How it works?
Any person can nominate a kids business from their local community to win free advertising at TotBramble for 2 months. The person that nominates the winning business will win a $100 TotBramble ValuePass.
To nominate a business the person needs only to write the business name and location on the facebook post comments.

The look and feel of the banner:
Clean but at the same time communicate the message effectively

Reason: Given my unavailability to provide immediate feedback, I am keen to extend the deadline so we have a bit more time to work on the banners. Cheers!

```html
<!DOCTYPE html>
<html lang="en">
<head>
<meta charset="utf-8">
<title>TotBramble – Nominate Your Favourite Local Kids Business</title>
<link rel="stylesheet" href="https://fonts.googleapis.com/css2?family=Oswald:wght@400;600;700&family=Roboto:wght@400;700&family=Permanent+Marker&display=swap">
<style>
  :root {
    --canvas-bg: #e8e8e6;
    --photo-light: #d9d8d4;
    --photo-mid: #c9c3b6;
    --photo-warm: #d8b98a;
    --teal: #2bbdd1;
    --pink: #f2687c;
    --ink: #1d1d1f;
    --navy: #2c3a4b;
    --white: #ffffff;
  }
  * { margin: 0; padding: 0; box-sizing: border-box; }
  html, body {
    width: 1200px;
    height: 444px;
    overflow: hidden;
    background: var(--canvas-bg);
  }
  .banner {
    position: relative;
    width: 1200px;
    height: 444px;
    overflow: hidden;
    background: var(--canvas-bg);
    font-family: "Oswald", "Arial Narrow", sans-serif;
  }
  .hero-photo {
    position: absolute;
    left: 0;
    top: 0;
    width: 640px;
    height: 444px;
    background:
      radial-gradient(ellipse 170px 210px at 420px 220px, var(--photo-warm) 0%, rgba(216,185,138,0.55) 45%, rgba(216,185,138,0) 100%),
      linear-gradient(90deg, var(--photo-light) 0%, var(--photo-mid) 55%, var(--canvas-bg) 100%);
  }
  .prize-corner {
    position: absolute;
    left: 0;
    top: 0;
    width: 380px;
    height: 310px;
  }
  .prize-corner text {
    font-family: "Oswald", "Arial Narrow", sans-serif;
    font-size: 24px;
    font-weight: 700;
    fill: var(--white);
    text-anchor: middle;
    letter-spacing: 0.5px;
  }
  .headline-script {
    position: absolute;
    left: 775px;
    top: 18px;
    font-family: "Permanent Marker", "Comic Sans MS", cursive;
    font-size: 38px;
    line-height: 50px;
    color: var(--ink);
    transform: rotate(-2deg);
    letter-spacing: 1px;
    white-space: nowrap;
  }
  .headline-ribbon {
    position: absolute;
    left: 629px;
    top: 86px;
    width: 571px;
    height: 72px;
  }
  .headline-ribbon svg { position: absolute; inset: 0; width: 100%; height: 100%; }
  .headline-ribbon span {
    position: absolute;
    left: 18px;
    right: 0;
    top: 0;
    font-size: 41px;
    font-weight: 400;
    line-height: 72px;
    text-align: center;
    color: var(--ink);
    letter-spacing: 0.3px;
    white-space: nowrap;
  }
  .offer-copy {
    position: absolute;
    right: 24px;
    top: 190px;
    font-family: "Roboto", Arial, sans-serif;
    font-size: 30px;
    font-weight: 400;
    line-height: 41px;
    text-align: right;
    color: var(--navy);
    white-space: nowrap;
  }
  .offer-copy strong { font-weight: 700; }
  .dotted-rule {
    position: absolute;
    left: 576px;
    top: 307px;
    width: 604px;
    height: 10px;
  }
</style>
</head>
<body>
  <main class="banner">
    <div class="hero-photo" role="img" aria-label="Photo of a young child wearing a yellow hard hat, resting chin on hands, against a light grey background with faint toy doodles"></div>

    <svg class="prize-corner" viewBox="0 0 380 310" aria-label="The winning nominee receives a $100 TotBramble ValuePass">
      <polygon points="0,0 372,0 0,300" fill="var(--teal)"/>
      <g transform="translate(186 150) rotate(-38.9)">
        <text x="-7" y="-30">VALUEPASS</text>
        <text x="-13" y="-62">$100 TOTBRAMBLE</text>
        <text x="-20" y="-94">RECEIVES A</text>
        <text x="-26" y="-126">WINNING NOMINEE</text>
        <text x="-33" y="-158">★ THE</text>
      </g>
    </svg>

    <p class="headline-script">nominate your</p>

    <div class="headline-ribbon">
      <svg viewBox="0 0 571 72" preserveAspectRatio="none" aria-hidden="true">
        <polygon points="0,0 571,0 571,72 0,72 14,63 0,54 14,45 0,36 14,27 0,18 14,9" fill="var(--pink)"/>
      </svg>
      <span>FAVOURITE LOCAL KIDS BUSINESS</span>
    </div>

    <p class="offer-copy">
      TO GIVE THEM THE CHANCE TO WIN<br>
      <strong>FREE AD PLACEMENT</strong> ON TOTBRAMBLE<br>
      WEBSITE FOR TWO MONTHS.
    </p>

    <svg class="dotted-rule" viewBox="0 0 604 10" aria-hidden="true">
      <line x1="4" y1="5" x2="600" y2="5" stroke="var(--navy)" stroke-width="5" stroke-linecap="round" stroke-dasharray="0 11"/>
    </svg>
  </main>
</body>
</html>
```